Business Card Design

I need a business card design for my new solo law practice. I practice consumer bankruptcy law.

I would like a simple, functional business card that looks professional but will also be understandable to regular people - not just other lawyers.
Updates

I added a couple of possible logos that can be incorporated

I'm sorry about the confusion, but the suite number for my new office is suite #150. Thanks for your patience

Target Market(s)

the real target market is potential clients

Industry/Entity Type

Business

Contact Information for Business Card

Law Offices of Dorian P. Whitcombe
Dorian P. Whitcombe
Attorney at Law
Bankruptcy Law
487 Mariner Court #150
Westbrook, OH 44102
(555) 318-7264 (Phone)
(555) 318-7290 (Fax)
dorianw@fernleydebtrelief.example
fernleydebtrelief.example

Font styles to use
Serif

Requirements
Nice to have
• I've added some possible logos to possible incorporate

```html
<!DOCTYPE html>
<html lang="en">
<head>
<meta charset="utf-8">
<title>Dorian P. Whitcombe – Business Card</title>
<link rel="stylesheet" href="https://fonts.googleapis.com/css2?family=Ovo&display=swap">
<style>
  :root {
    --navy: #23456b;
    --ink: #2b4a6f;
    --paper: #ffffff;
  }
  html, body {
    margin: 0;
    padding: 0;
    overflow: hidden;
    background: var(--paper);
  }
  .card {
    position: relative;
    width: 1200px;
    height: 702px;
    background: var(--paper);
    font-family: "Ovo", Georgia, serif;
    color: var(--ink);
    overflow: hidden;
  }
  .brand-mark {
    position: absolute;
    left: 53px;
    top: 47px;
    width: 178px;
    height: 178px;
  }
  .firm-name {
    position: absolute;
    left: 247px;
    top: 100px;
    margin: 0;
    font-size: 56px;
    line-height: 80px;
    font-weight: 400;
    color: var(--navy);
    white-space: nowrap;
  }
  .attorney {
    position: absolute;
    right: 50px;
    top: 268px;
    text-align: right;
  }
  .attorney-name {
    margin: 0;
    font-size: 55px;
    line-height: 62px;
    font-weight: 400;
    color: var(--navy);
    white-space: nowrap;
  }
  .attorney-line {
    margin: 0;
    font-size: 34px;
    line-height: 39px;
    white-space: nowrap;
  }
  .address {
    position: absolute;
    left: 53px;
    top: 539px;
    font-style: normal;
    font-size: 35px;
    line-height: 39px;
  }
  .contact {
    position: absolute;
    right: 50px;
    top: 578px;
    text-align: right;
    font-size: 35px;
    line-height: 39px;
  }
  .line { display: block; white-space: nowrap; }
</style>
</head>
<body>
<main class="card">
  <svg class="brand-mark" viewBox="0 0 178 178" aria-hidden="true">
    <circle cx="89" cy="89" r="84" fill="none" stroke="var(--navy)" stroke-width="10"/>
  </svg>
  <h1 class="firm-name">Law Offices of Dorian P. Whitcombe</h1>

  <section class="attorney">
    <h2 class="attorney-name">Dorian P. Whitcombe</h2>
    <p class="attorney-line">Attorney at Law Bankruptcy Law</p>
    <p class="attorney-line">dorianw@fernleydebtrelief.example</p>
  </section>

  <address class="address">
    <span class="line">487 Mariner Court</span>
    <span class="line">#150 Westbrook, OH 44102</span>
    <span class="line">www.fernleydebtrelief.example</span>
  </address>

  <div class="contact">
    <span class="line">Phone:&nbsp; (555) 318–7264</span>
    <span class="line">Fax: (555) 318–7290</span>
  </div>
</main>
</body>
</html>
```